Verdanix Medical Business Card

Create a high class Business card for Medical Aesthetics and Wellness Practice called Verdanix Medical Aesthetics and Wellness as per the logo attached.
Addresss is: 418 Harlan Brook Road Suite 312 Melville, New York 11093
Phone (555)204-7391 IG @verdanix_medical
Verdanixmedical.example

I need 5 different name configurations
1) Dr. Theo Valcourt
Aesthetics and Wellness Specialist
Medical Director

2) Rosalind Pettinger, NP
Clinical Nurse Manager

3) Marla Vostrik, RN
Aesthetic Nurse Specialist

4) Petra Halvesen, RN

5) Dana Kowbeck, L.E.
Senior Licensed Esthetician

Target Market(s)

22-55 Females

Industry/Entity Type

Medical Spa and Wellness

Contact Information for Business Card

Logo, address, phone, web, instagram, providers name

Requirements
Must have
• Attractive classy modern look

```html
<!DOCTYPE html>
<html lang="en">
<head>
<meta charset="UTF-8">
<title>Verdanix Medical Business Card</title>
<link href="https://fonts.googleapis.com/css2?family=Montserrat:wght@300;400;500;700&display=swap" rel="stylesheet">
<style>
  :root {
    --teal: #124f5f;
    --frame: #2e2e2e;
    --paper: #ffffff;
    --ink: #2b2b2b;
    --page: #ffffff;
  }
  * { margin: 0; padding: 0; box-sizing: border-box; }
  html, body {
    width: 1200px; height: 1000px; overflow: hidden;
    background: var(--page);
    font-family: "Montserrat", Arial, sans-serif;
  }
  .card-frame {
    position: absolute; left: 297px; width: 606px; height: 363px;
    background: var(--frame);
  }
  .card-frame--front { top: 120px; }
  .card-frame--back { top: 516px; }
  .card {
    position: absolute; left: 21px; top: 21px; width: 564px; height: 322px;
    overflow: hidden;
  }
  .card--front { background: var(--paper); }
  .card--back { background: var(--teal); }

  .holder-name {
    position: absolute; left: 35px; top: 45px;
    font-size: 23px; font-weight: 700; color: var(--teal); letter-spacing: 0.2px;
  }
  .holder-role {
    position: absolute; left: 35px; top: 75px;
    font-size: 13.5px; font-weight: 500; color: var(--ink);
  }
  .address {
    position: absolute; left: 35px; top: 168px;
    font-size: 14.5px; line-height: 16.5px; font-weight: 400; color: var(--ink);
  }
  .contact-list {
    position: absolute; left: 35px; top: 214px; list-style: none;
  }
  .contact-item {
    display: flex; align-items: center; height: 24px;
    font-size: 13px; color: var(--ink);
  }
  .contact-icon { width: 18px; height: 18px; margin-right: 11px; flex: none; }

  .brand {
    position: absolute; text-align: center; color: var(--teal);
    font-family: "Montserrat", Arial, sans-serif; font-weight: 300;
  }
  .brand-name, .brand-tagline, .brand-place { line-height: 1; white-space: nowrap; }

  .brand--front { left: 346px; top: 225px; width: 196px; }
  .brand--front .brand-name { font-size: 30px; letter-spacing: 4px; }
  .brand--front .brand-tagline { font-size: 7.5px; margin-top: 7px; letter-spacing: 0.2px; }
  .brand--front .brand-place { font-size: 6px; margin-top: 8px; letter-spacing: 4px; }

  .brand--back { left: 0; top: 104px; width: 564px; color: var(--paper); }
  .brand--back .brand-name { font-size: 56px; letter-spacing: 10px; }
  .brand--back .brand-tagline { font-size: 14.5px; margin-top: 15px; letter-spacing: 0.5px; }
  .brand--back .brand-place { font-size: 10px; margin-top: 13px; letter-spacing: 8px; }

  .wave { position: absolute; left: 0; top: 0; width: 564px; height: 322px; }
</style>
</head>
<body>
  <div class="card-frame card-frame--front">
    <section class="card card--front">
      <h1 class="holder-name">Rosalind Pettinger, NP</h1>
      <p class="holder-role">Clinical Nurse Manager</p>
      <p class="address">418 Harlan Brook Road Suite 312<br>Melville, New York 11093</p>
      <ul class="contact-list">
        <li class="contact-item">
          <svg class="contact-icon" viewBox="0 0 24 24" aria-hidden="true">
            <path d="M6.6 2.5 L9.5 6.5 L7.8 9 C8.8 11.5 11 13.8 14 15.2 L16.5 13.5 L20.5 16.5 L18.5 20.5 C11 20 4 13 3.5 5.5 Z" fill="var(--teal)"/>
            <path d="M14 3 A7 7 0 0 1 21 10" fill="none" stroke="var(--teal)" stroke-width="1.8"/>
            <path d="M14 6.5 A3.5 3.5 0 0 1 17.5 10" fill="none" stroke="var(--teal)" stroke-width="1.8"/>
          </svg>
          (555)204-7391
        </li>
        <li class="contact-item">
          <svg class="contact-icon" viewBox="0 0 24 24" aria-hidden="true">
            <rect x="2" y="2" width="20" height="20" rx="3" fill="var(--teal)"/>
          </svg>
          @verdanix_medical
        </li>
        <li class="contact-item">
          <svg class="contact-icon" viewBox="0 0 24 24" aria-hidden="true">
            <circle cx="12" cy="12" r="10" fill="var(--teal)"/>
            <g fill="none" stroke="var(--paper)" stroke-width="1.3">
              <ellipse cx="12" cy="12" rx="4.5" ry="10"/>
              <line x1="12" y1="2" x2="12" y2="22"/>
              <line x1="2" y1="12" x2="22" y2="12"/>
              <line x1="3.5" y1="7.5" x2="20.5" y2="7.5"/>
              <line x1="3.5" y1="16.5" x2="20.5" y2="16.5"/>
            </g>
          </svg>
          Verdanixmedical.example
        </li>
      </ul>
      <div class="brand brand--front">
        <div class="brand-name">Verdanix</div>
        <div class="brand-tagline">MEDICAL AESTHETICS AND WELLNESS</div>
        <div class="brand-place">NEW YORK</div>
      </div>
      <svg class="wave" viewBox="0 0 564 322" aria-hidden="true">
        <path d="M0 301 L338 301 C332 304 322 308 312 308 L0 308 Z" fill="var(--teal)"/>
        <path d="M564 294 L382 294 C368 294 360 298 350 304 C336 311 326 313 312 313 L0 313 L0 322 L564 322 Z" fill="var(--teal)"/>
      </svg>
    </section>
  </div>

  <div class="card-frame card-frame--back">
    <section class="card card--back">
      <div class="brand brand--back">
        <div class="brand-name">Verdanix</div>
        <div class="brand-tagline">MEDICAL AESTHETICS AND WELLNESS</div>
        <div class="brand-place">NEW YORK</div>
      </div>
    </section>
  </div>
</body>
</html>
```